Corporate Design für Make Up Artist
Zielgruppe
Ich bin Make-up Artist und arbeite sehr viel B2B, aber auch teilweise B2C.
Im B2C Bereich ist meine Zielgruppe: Frauen im Alter von Ende 20 bis Ende 30, die sich gerne etwas gönnen, die viel Wert auf Schönheit legen und dabei nicht auf den Preis schauen, womit ich mich auch deutlich abheben möchte.
Im B2B sind es Geschäftskunden, die auf den ersten Blick meine Professionalität erkennen sollen.
Aufgabenstellung
Ich suche ein hochwertiges Design, das meine professionelle Arbeit, Vertrauen, Modernität und Exklusivität widerspiegelt.
Der Name LUMORA setzt sich aus dem spanischen Wort `Viveza`(=Lebendigkeit) und meinem Vornamen Korinna zusammen.
Dabei sind die Logos von Duroque, Henri Lacombe und der Mirelle meine Vorbilder.
Ich möchte keinesfalls kindliche Verschnörkelungen oder ähnliches. Mein Logo soll ein Statement setzen und im Gedächtnis bleiben.
Zudem möchte ich in Zukunft eigene Produkte im Beauty Segment auf den Markt bringen.
Die Farben, die mich persönlich widerspiegeln sind schwarz und gold.
Ich habe ein Logo hochgeladen, dass mich sehr anspricht, wo aber der nötige USP fehlt.
Bin aber auch für andere Vorschläge offen.

```html
<!DOCTYPE html>
<html lang="de">
<head>
<meta charset="utf-8">
<title>LUMORA – Geschäftsausstattung</title>
<link rel="stylesheet" href="https://fonts.googleapis.com/css2?family=Open+Sans:wght@400;600&family=Oswald:wght@500&display=swap">
<style>
  :root {
    --ink: #000000;
    --paper: #ffffff;
    --stage: #e6e6e6;
    --gold: #c9a43a;
    --card: #2c3038;
    --text: #111111;
  }
  * { box-sizing: border-box; margin: 0; padding: 0; }
  html, body { width: 1200px; height: 2677px; overflow: hidden; }
  body {
    position: relative;
    background: var(--stage);
    font-family: "Open Sans", sans-serif;
    color: var(--text);
  }

  /* Letterhead */
  .letterhead {
    position: absolute; left: 79px; top: 77px;
    width: 1045px; height: 1478px;
    background: var(--paper); overflow: hidden;
  }
  .brand-block {
    position: absolute; left: 129px; top: 0;
    width: 237px; height: 237px; background: var(--ink);
    display: flex; align-items: center; justify-content: center;
  }
  .brand-name {
    font-family: "Open Sans", sans-serif; font-weight: 600;
    letter-spacing: 0.22em; color: var(--gold);
  }
  .brand-block .brand-name { font-size: 26px; }
  .rule-gold { position: absolute; left: 129px; top: 247px; width: 237px; height: 10px; background: var(--gold); }
  .rule-left { position: absolute; left: 0; top: 248px; width: 89px; height: 9px; background: var(--ink); }
  .rule-right { position: absolute; left: 404px; top: 248px; width: 641px; height: 9px; background: var(--ink); }

  .contact-row {
    position: absolute; left: 418px; top: 163px;
    display: flex; align-items: center;
    font-size: 13.5px; line-height: 18px;
  }
  .contact-group { display: grid; grid-template-columns: 16px auto; column-gap: 10px; align-items: center; padding: 0 20px; }
  .contact-group:first-child { padding-left: 0; }
  .contact-group + .contact-group { border-left: 2px solid var(--ink); }
  .contact-group svg { width: 12px; height: 12px; }
  .contact-group .pin { grid-row: span 2; }

  .letter-heading {
    position: absolute; left: 128px; top: 440px;
    font-family: "Oswald", sans-serif; font-weight: 500;
    font-size: 42px; letter-spacing: -0.01em; line-height: 1;
  }
  .letter-body { position: absolute; left: 128px; top: 512px; width: 700px; font-size: 22px; line-height: 30.5px; }
  .letter-body p + p { margin-top: 10px; }

  .signature-role { position: absolute; left: 145px; top: 1224px; font-size: 25px; }
  .signature-name { position: absolute; left: 145px; top: 1334px; font-size: 25px; }
  .signature-line { position: absolute; left: 132px; top: 1403px; width: 782px; height: 4px; background: var(--ink); }
  .footer-band { position: absolute; left: 132px; top: 1447px; width: 782px; height: 31px; background: var(--ink); }

  /* Logo panels */
  .logo-panel {
    position: absolute; top: 1555px; height: 395px;
    display: flex; align-items: center; justify-content: center;
  }
  .logo-panel .brand-name { font-size: 44px; }
  .logo-panel--light { left: 0; width: 574px; background: var(--paper); }
  .logo-panel--light .brand-name { color: var(--ink); }
  .logo-panel--dark { left: 574px; width: 549px; background: var(--ink); }

  /* Embossed card presentation, flat */
  .card-panel {
    position: absolute; left: 77px; top: 1950px; width: 1046px; height: 720px;
    background: var(--card);
    display: flex; align-items: center; justify-content: center;
  }
  .card-panel .brand-name { font-size: 64px; }
</style>
</head>
<body>

<section class="letterhead">
  <div class="brand-block"><span class="brand-name">LUMORA</span></div>
  <div class="rule-left"></div>
  <div class="rule-gold"></div>
  <div class="rule-right"></div>

  <div class="contact-row">
    <div class="contact-group">
      <svg class="pin" viewBox="0 0 12 12" aria-hidden="true"><path d="M6 0a4 4 0 0 0-4 4c0 3 4 7 4 7s4-4 4-7a4 4 0 0 0-4-4zm0 5.5a1.5 1.5 0 1 1 0-3 1.5 1.5 0 0 1 0 3z"/><rect x="2" y="11" width="8" height="1"/></svg>
      <span>Lindenhofweg 14 b</span>
      <span>45127 Ruhrstadt</span>
    </div>
    <div class="contact-group">
      <svg viewBox="0 0 12 12" aria-hidden="true"><path d="M2.5 0.5l2 2-1.2 1.6c.8 1.6 2 2.8 3.6 3.6L8.5 6.5l2 2L9 11C4.5 10.5 1 7 0.5 2.5z"/></svg>
      <span>0201-5550142</span>
      <svg viewBox="0 0 12 12" aria-hidden="true"><rect x="3" y="0.5" width="6" height="11" rx="1" fill="none" stroke="#000"/><rect x="5" y="9" width="2" height="1"/></svg>
      <span>0170-5550199</span>
    </div>
    <div class="contact-group">
      <svg viewBox="0 0 12 12" aria-hidden="true"><rect x="0.5" y="2.5" width="11" height="8" fill="none" stroke="#000"/><path d="M0.5 2.5L6 7l5.5-4.5" fill="none" stroke="#000"/></svg>
      <span>mail@lumora-studio.de</span>
      <svg viewBox="0 0 12 12" aria-hidden="true"><circle cx="6" cy="6" r="5.5" fill="none" stroke="#000"/><ellipse cx="6" cy="6" rx="2.5" ry="5.5" fill="none" stroke="#000"/><path d="M0.5 6h11" stroke="#000"/></svg>
      <span>www.lumora-studio.de</span>
    </div>
  </div>

  <h1 class="letter-heading">YOUR TEXT HERE</h1>
  <div class="letter-body">
    <p>Lorem ipsum dolor sit amet, consectetur adipiscing elit.<br>Etiam iaculis dolor a ligula tincidunt, a aliquet nulla porta.<br>Quisque eget arcu metus.<br>Suspendisse potenti.</p>
    <p>Sed non libero sed mauris placerat venenatis.<br>Quisque mauris nunc, gravida ut nunc at, egestas<br>Suspendisse nec turpis sem.<br>Cras vehicula ut diam nec cursus.</p>
    <p>Mauris accumsan rhoncus justo, vitae sollicitudin<br>Vivamus a maximus nisl.<br>Nulla facilisi.<br>Morbi posuere leo lacus, at interdum enim viverra ut.<br>Nullam id mattis augue.</p>
    <p>Nulla rutrum maximus egestas.<br>Cum sociis natoque penatibus et magnis dis parturient<br>Vivamus facilisis sem sed magna semper, id aliquam.<br>Nullam faucibus arcu et arcu feugiat luctus</p>
  </div>

  <p class="signature-role">General Manager</p>
  <p class="signature-name">tobu velden</p>
  <div class="signature-line"></div>
  <div class="footer-band"></div>
</section>

<section class="logo-panel logo-panel--light"><span class="brand-name">LUMORA</span></section>
<section class="logo-panel logo-panel--dark"><span class="brand-name">LUMORA</span></section>

<section class="card-panel"><span class="brand-name">LUMORA</span></section>

</body>
</html>
```